I am a company selling interior designing materials

HI, I am selling interior design materials and require a namecard which is more outstanding while following a certain details placement as attached.

My clients are mainly interior designers so it has to attract their attention rather than feeling that its "just another namecard". I am selling wallcoverings, fabrics, acoustics and carpets.

Target Market(s)

interior designers designing hotels, commerical offices.

Contact Information for Business Card

As per attached.
Please change address to 47 Jalan 16 Tampines #05-02 Velmora Building Singapore 527314

Font styles to use
Other font styles liked:
• calibri

Requirements
Must have
• (1) company logo on top in the middle. Placement of contac details to be the same
• (2) company color is blue/green cymk 75/8/42/0
• (3) "KTV" logo to be prominent
• (4) You may change the logo but there should be a "swirl" surrounding the word KTV like current logo. The swirl pattern does not need to follow current logo and you may propose.
Should not have
• (1) there should not be any designs above "KTV" logo
• (2) no sharp triangles or angles

```html
<!DOCTYPE html>
<html lang="en">
<head>
<meta charset="utf-8">
<title>KTV Business Card</title>
<link href="https://fonts.googleapis.com/css2?family=Carlito:wght@400;700&display=swap" rel="stylesheet">
<style>
  :root {
    --backdrop: #2b2b2d;
    --card-top: #1c1c1d;
    --card-bottom: #0c0c0d;
    --teal: #1fb0a3;
    --grey: #6d6d6f;
    --white: #f4f4f4;
    --red: #d3262b;
    --divider: #555558;
  }
  * { margin: 0; padding: 0; box-sizing: border-box; }
  html, body {
    width: 1200px; height: 900px; overflow: hidden;
    background: var(--backdrop);
    font-family: "Carlito", "Calibri", sans-serif;
  }
  .stage { position: relative; width: 1200px; height: 900px; }
  .card {
    position: absolute; left: 280px; width: 640px; height: 366px;
    background: linear-gradient(160deg, var(--card-top), var(--card-bottom));
    overflow: hidden;
  }
  .card--front { top: 52px; }
  .card--back { top: 470px; }
  .card__band {
    position: absolute; left: 0; right: 0; bottom: 0; height: 11px;
    background: var(--teal);
  }

  /* Front */
  .brand {
    position: absolute; top: 92px; left: 0; right: 0;
    text-align: center;
  }
  .brand__mark {
    display: inline-flex; align-items: center; gap: 14px;
    font-size: 58px; font-weight: 700; color: var(--grey); letter-spacing: 2px;
    line-height: 1;
  }
  .brand__dot {
    width: 16px; height: 16px; border-radius: 50%; background: var(--teal);
  }
  .brand__company {
    margin-top: 14px;
    font-size: 19px; font-weight: 700; color: var(--grey);
  }
  .services {
    position: absolute; left: 0; right: 0; bottom: 60px;
    text-align: center; font-size: 21px; color: var(--white);
  }
  .services__sep { color: var(--red); margin: 0 6px; }

  /* Back */
  .person {
    position: absolute; left: 120px; top: 108px;
    font-size: 31px; color: var(--teal);
  }
  .divider {
    position: absolute; left: 330px; top: 100px; width: 1px; height: 110px;
    background: var(--divider);
  }
  .contacts {
    position: absolute; left: 350px; top: 118px; list-style: none;
    font-size: 19px; color: var(--white);
  }
  .contacts__item { display: flex; align-items: center; gap: 8px; margin-bottom: 6px; }
  .contacts__icon { width: 14px; height: 14px; flex: none; }
  .address {
    position: absolute; left: 0; right: 0; bottom: 92px;
    text-align: center; font-size: 19px; color: var(--white);
  }
</style>
</head>
<body>
<main class="stage">

  <section class="card card--front">
    <div class="brand">
      <div class="brand__mark"><span class="brand__dot"></span>KTV</div>
      <div class="brand__company">KaTaVell Interior Furnishings Pte Ltd</div>
    </div>
    <p class="services">
      Wallcoverings<span class="services__sep">|</span>Acoustic<span class="services__sep">|</span>Fabrics<span class="services__sep">|</span>Carpet
    </p>
    <div class="card__band"></div>
  </section>

  <section class="card card--back">
    <h1 class="person" style="font-weight:400">Lorna Tay</h1>
    <div class="divider"></div>
    <ul class="contacts">
      <li class="contacts__item">
        <svg class="contacts__icon" viewBox="0 0 16 16" aria-hidden="true"><path fill="#1fb0a3" d="M1 5c0-2 3-3 7-3s7 1 7 3v1.5h-3.5V5H4.5v1.5H1zM3.5 7h9l1.5 6.5H2z"/><circle cx="8" cy="10.2" r="1.8" fill="#111"/></svg>
        (65)9172 4410
      </li>
      <li class="contacts__item">
        <svg class="contacts__icon" viewBox="0 0 16 16" aria-hidden="true"><rect x="4" y="1" width="8" height="14" rx="1.5" fill="none" stroke="#1fb0a3" stroke-width="1.6"/><circle cx="8" cy="12.3" r="0.9" fill="#1fb0a3"/></svg>
        (65)6281 5073
      </li>
      <li class="contacts__item">
        <svg class="contacts__icon" viewBox="0 0 16 16" aria-hidden="true"><rect x="1" y="3" width="14" height="10" rx="1" fill="#1fb0a3"/><path d="M1.5 3.8 8 9l6.5-5.2" fill="none" stroke="#111" stroke-width="1.2"/></svg>
        lorna@ktvfurnishings.com
      </li>
    </ul>
    <p class="address">47 Jalan 16 Tampines #05-02 Velmora Building Singapore 527314</p>
    <div class="card__band"></div>
  </section>

</main>
</body>
</html>
```